Mission Vision and Values Infographic

We are a healthcare organisation and would like to create a graphic which showcases our Mission, Vision and Values in a clear and beautiful manner.

Attached is:

* Our mission vision and values.
* Style Guide
* Examples of other designs found on the web
* Logo

Your design should be Simple, Clear, Professional and Beautiful.

If you prefer, you can submit a Basic design to start off with for initial feedback before then refining in a future submission. Please check back in the comments section as I will be providing additional general remarks if needed.

The design needs to be created in a tool which will then allow us to modify it in the future…. Ideally either Adobe InDesign, Adobe Illustrator or Adobe Photoshop. Vector is preferred.

All together, the whole design needs to be:

* Printable on one sheet of A3 size paper (to go on our wall)
* Be able to go on a webpage

So there might be slight variations for bigger and smaller displays. For example, the A3 Page will have all three - Mission, Vision and Values + Logo together. The version for a webpage might be separated into 3 parts to make it easier to show on a webpage.

Good luck and happy designing

```html
<!DOCTYPE html>
<html lang="en">
<head>
<meta charset="utf-8">
<title>Mission, Vision and Values</title>
<link href="https://fonts.googleapis.com/css2?family=Montserrat:wght@500;700;800&family=Open+Sans:wght@400;600&display=swap" rel="stylesheet">
<style>
  :root{
    --navy:#1d3e74;
    --navy-deep:#183564;
    --sky:#2aa5df;
    --gold:#f2b530;
    --white:#ffffff;
    --ink:#2b3a55;
  }
  *{box-sizing:border-box;margin:0;padding:0}
  html,body{width:1200px;height:848px;overflow:hidden;background:var(--navy)}
  .sheet{position:relative;width:1200px;height:848px;background:var(--navy);font-family:"Open Sans",Arial,sans-serif;overflow:hidden}

  .statement{position:absolute;top:27px;width:568px;height:213px;background:var(--white);border:4px solid var(--gold);border-radius:14px;overflow:hidden;display:flex}
  .statement--mission{left:23px}
  .statement--vision{left:609px}
  .statement__icon{position:relative;width:133px;flex:none;background:var(--sky);display:flex;align-items:center;justify-content:center}
  .statement__icon::after{content:"";position:absolute;right:-16px;top:18px;border-left:16px solid var(--sky);border-top:16px solid transparent;border-bottom:16px solid transparent}
  .statement__body{padding:20px 22px 0 36px}
  .statement__title{font-family:"Montserrat",Arial,sans-serif;font-weight:800;font-size:23px;color:var(--navy);letter-spacing:.3px;margin-bottom:10px}
  .statement__text{font-size:14.6px;line-height:1.3;color:var(--ink)}

  .pillars{position:absolute;left:0;top:287px;width:1200px;height:110px;background:var(--sky);display:flex}
  .pillar{position:absolute;top:0;height:110px;display:flex;align-items:center}
  .pillar--enable{left:73px}
  .pillar--empower{left:433px}
  .pillar--educate{left:820px}
  .pillar__badge{width:80px;height:80px;border-radius:50%;background:var(--gold);border:4px solid var(--navy);box-shadow:0 0 0 3px var(--sky),0 0 0 5px var(--navy);display:flex;align-items:center;justify-content:center;margin-right:22px}
  .pillar__label{font-family:"Montserrat",Arial,sans-serif;font-weight:800;font-size:27px;line-height:1.08;color:var(--navy);letter-spacing:.4px}

  .values{position:absolute;left:0;top:397px;width:1200px;height:451px}
  .value{position:absolute;width:300px}
  .value--left{left:12px;text-align:right}
  .value--right{left:896px;text-align:left}
  .value__name{font-family:"Montserrat",Arial,sans-serif;font-weight:800;font-size:23px;color:var(--gold);letter-spacing:.3px;margin-bottom:3px}
  .value__text{font-size:11px;line-height:1.25;color:var(--white)}

  .value-icon{position:absolute;width:92px;height:92px;border-radius:50%;background:var(--white);border:4px solid var(--navy-deep);box-shadow:0 0 0 3px var(--sky);display:flex;align-items:center;justify-content:center}

  .core{position:absolute;left:523px;top:146px;width:154px;height:154px;border-radius:50%;background:var(--white);display:flex;align-items:center;justify-content:center;text-align:center;font-family:"Montserrat",Arial,sans-serif;font-weight:700;font-size:31px;line-height:1.12;color:var(--navy)}
  .connectors{position:absolute;left:0;top:0}

  .brand{position:absolute;left:540px;top:384px;display:flex;align-items:center;gap:8px}
  .brand__dot{width:26px;height:26px;border-radius:50%;border:2.5px solid var(--white)}
  .brand__name{font-family:"Montserrat",Arial,sans-serif;font-weight:700;font-size:12.5px;line-height:1.1;color:var(--white)}
</style>
</head>
<body>
<main class="sheet">

  <section class="statement statement--mission">
    <div class="statement__icon">
      <svg width="72" height="72" viewBox="0 0 72 72" aria-hidden="true">
        <path d="M4 66 L28 28 L36 38 L44 26 L68 66 Z" fill="var(--navy)"/>
        <path d="M22 38 L28 28 L32 34 L27 40 Z" fill="var(--white)"/>
        <rect x="33" y="6" width="3" height="22" fill="var(--navy)"/>
        <path d="M36 6 H52 L47 11 L52 16 H36 Z" fill="var(--navy)"/>
      </svg>
    </div>
    <div class="statement__body">
      <h2 class="statement__title">OUR MISSION</h2>
      <p class="statement__text">At Harbourline Speech Studio we strive to ensure our clients and families have access to high quality, evidence-based intervention from a passionate and professional team to improve and develop individual functional skills that contribute to successful participation in the community.</p>
    </div>
  </section>

  <section class="statement statement--vision">
    <div class="statement__icon">
      <svg width="80" height="80" viewBox="0 0 80 80" aria-hidden="true">
        <g stroke="var(--navy)" stroke-width="4" stroke-linecap="round">
          <line x1="40" y1="8" x2="40" y2="17"/><line x1="24" y1="12" x2="28" y2="20"/><line x1="56" y1="12" x2="52" y2="20"/>
          <line x1="10" y1="22" x2="16" y2="28"/><line x1="70" y1="22" x2="64" y2="28"/>
          <line x1="40" y1="72" x2="40" y2="63"/><line x1="24" y1="68" x2="28" y2="60"/><line x1="56" y1="68" x2="52" y2="60"/>
        </g>
        <path d="M6 40 Q40 12 74 40 Q40 68 6 40 Z" fill="none" stroke="var(--navy)" stroke-width="5"/>
        <circle cx="40" cy="40" r="12" fill="var(--navy)"/>
        <circle cx="40" cy="40" r="5" fill="var(--sky)"/>
      </svg>
    </div>
    <div class="statement__body">
      <h2 class="statement__title">OUR VISION</h2>
      <p class="statement__text">Individuals of all abilities will have the opportunity to achieve their therapy goals by accessing gold standard services, so they may confidently participate in the wider community where they will be understood, supported and embraced for their individuality.</p>
    </div>
  </section>

  <section class="pillars">
    <div class="pillar pillar--enable">
      <div class="pillar__badge">
        <svg width="40" height="40" viewBox="0 0 40 40" aria-hidden="true"><path d="M6 21 L16 31 L35 9" fill="none" stroke="var(--navy)" stroke-width="6" stroke-linecap="round" stroke-linejoin="round"/></svg>
      </div>
      <div class="pillar__label">ENABLING<br>CLIENTS</div>
    </div>
    <div class="pillar pillar--empower">
      <div class="pillar__badge">
        <div role="img" aria-label="Family icon" style="width:38px;height:38px;border-radius:50%;background:var(--navy)"></div>
      </div>
      <div class="pillar__label">EMPOWERING<br>FAMILIES</div>
    </div>
    <div class="pillar pillar--educate">
      <div class="pillar__badge">
        <svg width="44" height="36" viewBox="0 0 44 36" aria-hidden="true">
          <path d="M22 7 Q12 1 3 4 V30 Q12 27 22 33 Q32 27 41 30 V4 Q32 1 22 7 Z" fill="none" stroke="var(--navy)" stroke-width="3.5" stroke-linejoin="round"/>
          <line x1="22" y1="7" x2="22" y2="33" stroke="var(--navy)" stroke-width="3.5"/>
        </svg>
      </div>
      <div class="pillar__label">EDUCATING<br>COMMUNITIES</div>
    </div>
  </section>

  <section class="values">
    <svg class="connectors" width="1200" height="451" viewBox="0 0 1200 451" aria-hidden="true">
      <g fill="none" stroke="var(--gold)" stroke-width="3.5" stroke-linecap="round">
        <path d="M515 138 A120 120 0 0 0 515 308"/>
        <path d="M685 138 A120 120 0 0 1 685 308"/>
        <path d="M480 223 H445 M458 223 Q440 223 432 205 M458 223 Q440 223 432 241"/>
        <path d="M720 223 H755 M742 223 Q760 223 768 205 M742 223 Q760 223 768 241"/>
      </g>
      <g fill="var(--gold)">
        <path d="M515 138 l-2 -12 l12 6 Z"/><path d="M685 138 l2 -12 l-12 6 Z"/>
        <path d="M440 223 l10 -6 v12 Z"/><path d="M760 223 l-10 -6 v12 Z"/>
      </g>
    </svg>

    <div class="core">Our 6<br>Core<br>Values</div>

    <article class="value value--left" style="top:57px">
      <h3 class="value__name">INTEGRITY</h3>
      <p class="value__text">We care for and respect the needs and well-being of our families, our team and ourselves. We encourage openness, trust and honest communication at all times.</p>
    </article>
    <article class="value value--left" style="top:185px">
      <h3 class="value__name">DIVERSITY</h3>
      <p class="value__text">We embed diversity by<br>recognising, respecting and<br>appreciating differences in<br>our families and our team.</p>
    </article>
    <article class="value value--left" style="top:326px">
      <h3 class="value__name">FLEXIBILITY</h3>
      <p class="value__text">We are flexible in our problem solving and offer options and solutions for our families and team wherever we reasonably can.</p>
    </article>

    <article class="value value--right" style="top:57px">
      <h3 class="value__name">QUALITY</h3>
      <p class="value__text">We strive for excellence through evidence based practice, self-reflection, feedback and a continuous commitment to improvement and discovery both professionally and personally.</p>
    </article>
    <article class="value value--right" style="top:185px">
      <h3 class="value__name">POSITIVITY</h3>
      <p class="value__text">We lead ourselves ‘above<br>the line’ choosing to adopt<br>a positive, accountable and<br>solution-focused mindset.</p>
    </article>
    <article class="value value--right" style="top:326px">
      <h3 class="value__name">CREATIVITY</h3>
      <p class="value__text">We are innovative and collaborative, constantly working towards new and improved ways to support our clients, families and our team.</p>
    </article>

    <div class="value-icon" style="left:347px;top:50px">
      <svg width="52" height="52" viewBox="0 0 52 52" aria-hidden="true">
        <circle cx="26" cy="26" r="24" fill="var(--navy)"/>
        <g stroke="var(--white)" stroke-width="3"><line x1="26" y1="2" x2="26" y2="50"/><line x1="2" y1="26" x2="50" y2="26"/></g>
        <g fill="var(--white)"><circle cx="26" cy="14" r="4"/><circle cx="38" cy="26" r="4"/><circle cx="26" cy="38" r="4"/><circle cx="14" cy="26" r="4"/></g>
      </svg>
    </div>
    <div class="value-icon" style="left:347px;top:184px">
      <svg width="56" height="52" viewBox="0 0 56 52" aria-hidden="true">
        <g stroke="var(--navy)" stroke-width="2.5" fill="none">
          <circle cx="22" cy="10" r="7"/><line x1="18" y1="16" x2="12" y2="30"/><line x1="26" y1="16" x2="34" y2="30"/><line x1="19" y1="38" x2="32" y2="38"/>
          <circle cx="12" cy="38" r="8"/>
        </g>
        <circle cx="40" cy="38" r="9" fill="var(--navy)"/>
      </svg>
    </div>
    <div class="value-icon" style="left:347px;top:310px">
      <svg width="54" height="54" viewBox="0 0 54 54" aria-hidden="true">
        <g fill="none" stroke="var(--navy)" stroke-width="4" stroke-linecap="round" stroke-linejoin="round">
          <path d="M27 50 V22"/><path d="M20 12 L27 4 L34 12"/>
          <path d="M27 30 Q27 20 12 14"/><path d="M6 20 L10 12 L18 12"/>
          <path d="M27 30 Q27 20 42 14"/><path d="M48 20 L44 12 L36 12"/>
        </g>
      </svg>
    </div>

    <div class="value-icon" style="left:758px;top:50px">
      <svg width="50" height="56" viewBox="0 0 50 56" aria-hidden="true">
        <path d="M14 34 L8 54 L17 49 L21 56 L25 40 Z M36 34 L42 54 L33 49 L29 56 L25 40 Z" fill="var(--navy)"/>
        <path d="M25 2 L30 6 L37 5 L39 12 L45 16 L42 22 L45 29 L39 32 L37 39 L30 38 L25 42 L20 38 L13 39 L11 32 L5 29 L8 22 L5 16 L11 12 L13 5 L20 6 Z" fill="var(--navy)"/>
        <circle cx="25" cy="22" r="11" fill="none" stroke="var(--white)" stroke-width="2.5"/>
        <path d="M20 22 L24 26 L31 18" fill="none" stroke="var(--white)" stroke-width="3" stroke-linecap="round"/>
      </svg>
    </div>
    <div class="value-icon" style="left:758px;top:184px">
      <div role="img" aria-label="Meditation figure icon" style="width:50px;height:50px;border-radius:50%;background:var(--navy)"></div>
    </div>
    <div class="value-icon" style="left:758px;top:310px">
      <svg width="56" height="56" viewBox="0 0 56 56" aria-hidden="true">
        <g stroke="var(--navy)" stroke-width="3" stroke-linecap="round">
          <line x1="28" y1="2" x2="28" y2="8"/><line x1="10" y1="10" x2="14" y2="14"/><line x1="46" y1="10" x2="42" y2="14"/>
          <line x1="3" y1="26" x2="9" y2="26"/><line x1="53" y1="26" x2="47" y2="26"/>
        </g>
        <path d="M28 12 A13 13 0 0 0 20 35 V41 H36 V35 A13 13 0 0 0 28 12 Z" fill="var(--navy)"/>
        <rect x="21" y="44" width="14" height="4" rx="1" fill="var(--navy)"/>
        <rect x="23" y="50" width="10" height="4" rx="2" fill="var(--navy)"/>
      </svg>
    </div>

    <div class="brand">
      <span class="brand__dot"></span>
      <span class="brand__name">Harbourline<br>Speech Studio</span>
    </div>
  </section>

</main>
</body>
</html>
```